LEARN Business Skills so you can Earn a good living

size of the poster is 8”x 10.75" plus 0.25" bleed.
Please leave 1 inch on the bottoum for footer
I want a design a poster that will attract people's attention.
I appreciate a creative ad however the ad should not take away from being able to clearly read the text.
-I also appreciate a simple creative ad that is not too busy.
-you can use graphics, vectors, or pictures of real people.
-however, if you use real people it should be a white male that is wearing a white shirt and look like a professional person.

Target Market(s)

Potential young business people

Industry/Entity Type

education

Requirements
Must have
• easy to read the text
Nice to have
• I would like a "creative" simple ad that is easy to be read
Should not have
• pictures of women

```html
<!DOCTYPE html>
<html lang="en">
<head>
<meta charset="utf-8">
<title>Learn It To Earn It — Business Enrichment Course</title>
<link rel="stylesheet" href="https://fonts.googleapis.com/css2?family=Archivo+Black&family=Montserrat:ital,wght@0,400;0,500;1,800&family=Source+Sans+3:wght@400;600;700&display=swap">
<style>
  :root {
    --teal: #5bc5cf;
    --ink: #303640;
    --white: #ffffff;
    --photo-light: #d9dde3;
    --photo-dark: #8a97a8;
  }
  * { margin: 0; padding: 0; box-sizing: border-box; }
  html, body { width: 899px; height: 1200px; overflow: hidden; background: var(--white); }
  .poster { position: relative; width: 899px; height: 1200px; overflow: hidden; background: var(--white); font-family: "Source Sans 3", sans-serif; color: var(--ink); }
  .artwork { position: absolute; inset: 0; width: 899px; height: 1200px; }
  .headline { position: absolute; left: 78px; top: 392px; font-family: "Archivo Black", sans-serif; font-weight: 400; color: var(--white); text-transform: uppercase; }
  .headline-line { position: absolute; left: 0; display: block; white-space: nowrap; line-height: 1; letter-spacing: -1px; }
  .headline .accent { color: var(--teal); }
  .line-learn { top: 0; font-size: 64px; }
  .line-it-to { top: 67px; font-size: 79px; }
  .line-earn { top: 154px; font-size: 79px; }
  .line-it { top: 235px; font-size: 79px; }
  .course { position: absolute; left: 78px; top: 836px; width: 760px; }
  .course-title { color: var(--teal); font-weight: 700; font-size: 27px; line-height: 1; }
  .course-tagline { font-size: 26px; font-weight: 400; line-height: 1; margin-top: 8px; }
  .skills-title { color: var(--teal); font-weight: 700; font-size: 24px; line-height: 1; margin-top: 22px; }
  .skills-benefits { font-weight: 700; font-size: 21.5px; line-height: 1; margin-top: 8px; }
  .topics { margin-top: 13px; width: 740px; font-size: 12.6px; line-height: 16.5px; text-transform: uppercase; }
  .topics-line { display: block; white-space: nowrap; text-align: justify; text-align-last: justify; }
  .contact { position: absolute; left: 118px; top: 1098px; font-family: "Montserrat", sans-serif; color: var(--ink); }
  .contact-label { font-size: 22px; font-weight: 400; line-height: 1; letter-spacing: 0.5px; }
  .contact-phone { font-size: 30px; font-weight: 800; font-style: italic; line-height: 1; margin-top: 6px; }
  .contact-web { font-size: 16px; font-weight: 500; line-height: 1; margin-top: 6px; letter-spacing: 1px; }
  .address { position: absolute; left: 577px; top: 1126px; font-family: "Montserrat", sans-serif; font-style: normal; color: var(--white); font-size: 16.5px; line-height: 22px; letter-spacing: 0.5px; }
</style>
</head>
<body>
<div class="poster">
  <svg class="artwork" viewBox="0 0 899 1200" xmlns="http://www.w3.org/2000/svg">
    <defs>
      <linearGradient id="photoTone" x1="0" y1="0" x2="0" y2="1">
        <stop offset="0" stop-color="var(--photo-light)"/>
        <stop offset="1" stop-color="var(--photo-dark)"/>
      </linearGradient>
    </defs>
    <path class="photo-placeholder" role="img" aria-label="Photo of a smiling professional man in a plaid blazer holding an open laptop" d="M520 60 H760 V674 H470 V330 Q480 270 520 250 Z" fill="url(#photoTone)"/>
    <polygon class="band-top" points="0,0 353,0 428,93 308,239 0,239" fill="var(--teal)"/>
    <path class="band-bottom" d="M483 594 C540 650 600 674 670 674 H899 V815 H490 C462 815 442 806 420 780 L377 721 Z" fill="var(--teal)"/>
    <path class="headline-panel" d="M0 234 H250 C330 234 380 260 410 300 L515 440 C540 472 540 528 515 560 L410 700 C380 740 330 762 250 762 H0 Z" fill="var(--ink)"/>
    <path class="accent-line" d="M347 190 H412 C440 190 462 205 478 225 L816 674" fill="none" stroke="var(--teal)" stroke-width="2.5"/>
    <line class="accent-line" x1="211" y1="234" x2="483" y2="594" stroke="var(--teal)" stroke-width="2.5"/>
    <path class="outline-slash" d="M747 42 H789 Q800 42 808 53 L877 150 Q881 157 872 157 H830 Q819 157 811 146 L742 50 Q739 42 747 42 Z" fill="none" stroke="var(--ink)" stroke-width="3"/>
    <path class="footer-contact" d="M0 1068 H392 Q410 1068 418 1085 L470 1200 H0 Z" fill="var(--teal)"/>
    <path class="footer-address" d="M470 1200 L441 1112 Q437 1095 458 1095 H899 V1200 Z" fill="var(--ink)"/>
    <g class="pin-icon" transform="translate(556 1147)">
      <path d="M0 -12 C-6.5 -12 -10 -7.5 -10 -2.5 C-10 4 -3 10 0 14 C3 10 10 4 10 -2.5 C10 -7.5 6.5 -12 0 -12 Z" fill="var(--teal)"/>
      <circle cx="0" cy="-2.5" r="3.5" fill="var(--ink)"/>
    </g>
  </svg>

  <h1 class="headline">
    <span class="headline-line line-learn">Learn</span>
    <span class="headline-line line-it-to">It <span class="accent">To</span></span>
    <span class="headline-line line-earn accent">Earn</span>
    <span class="headline-line line-it">It</span>
  </h1>

  <section class="course">
    <h2 class="course-title">Business Enrichment Course</h2>
    <p class="course-tagline">A proven success of helping people in their livelihoods</p>
    <h3 class="skills-title">Business skills that will help you:</h3>
    <p class="skills-benefits">Get a quality job - start/grow your business-Increase your salary</p>
    <p class="topics">
      <span class="topics-line">Business Admiistration – Small Business Management - Finance - Investments - Computers - Accounting - Sales</span>
      <span class="topics-line">Marketing Project Management Interviewing Skills - Business Law - Negotiation – Public Speaking - Import/Export</span>
      <span class="topics-line">Information Technoloy -Distribution Marketing - Ledgerly - Real Estate - Health Care-Management - Shopverse</span>
    </p>
  </section>

  <div class="contact">
    <p class="contact-label">CONTACT US</p>
    <p class="contact-phone">0123 456 7890</p>
    <p class="contact-web">www.websitename.com</p>
  </div>

  <address class="address">
    Your Street Address Here,<br>New York City, Zip- 000
  </address>
</div>
</body>
</html>
```